Moravel Swim Stationary

Recently established Aquatics Club, with competitive swimming being a principal activity needs stationary, including business cards, letterhead and envelopes, application forms.
The designs shold incorporate the Club's logo. ( The colours are aqua and teal)
The statonary should be fun yet project a corporate image sufficient to attract potential sponsors.

Club members, sponsors, professional organisations.

Business

• Club Logo
Address & Telephone number

The letterhead must contain the Club's Mission Statement.
It can be incorporated in the "footer" on the page.

To provide aquatics programmes, for persons of all ages, that encourage physical fitness and wellness, build character and self-discipline, inspire camaraderie and promote civic mindedness and excellence.

```html
<!DOCTYPE html>
<html lang="en">
<head>
<meta charset="utf-8">
<title>Moravel Swim Stationery</title>
<link href="https://fonts.googleapis.com/css2?family=Open+Sans:wght@400;600;700&display=swap" rel="stylesheet">
<style>
:root{
  --teal:#1a978c;
  --teal-dark:#13786f;
  --orange:#f58220;
  --paper:#ffffff;
  --ink:#3a3a3a;
  --grey:#8a8a8a;
  --rule:#9b9b9b;
  --ground:#ece9e4;
  --faint:#e8ecec;
}
*{margin:0;padding:0;box-sizing:border-box}
html,body{width:1200px;height:393px;overflow:hidden;background:var(--ground)}
body{font-family:"Open Sans",Arial,sans-serif;color:var(--ink);position:relative}
.sheet,.envelope,.card{position:absolute;background:var(--paper);box-shadow:0 1px 3px rgba(0,0,0,.18);overflow:hidden}
.brand{font-weight:700;color:var(--orange);white-space:nowrap;line-height:1;display:flex;align-items:center;gap:3px}
.brand .dot{display:inline-block;border-radius:50%;background:var(--teal)}
.swoosh{position:absolute;left:0;bottom:0;width:100%}
.tiny{font-size:3.4px;line-height:1.45;color:var(--grey)}
.option-label{position:absolute;top:350px;font-size:17px;color:#333;transform:translateX(-50%)}

/* option 1 */
.letterhead-1{left:50px;top:40px;width:234px;height:302px}
.letterhead-1 .brand{position:absolute;left:19px;top:10px;font-size:11px}
.mission-top{position:absolute;left:108px;top:11px;width:112px}
.mission-top h4,.mission-foot h4{font-size:5px;color:var(--orange);font-weight:700;margin-bottom:2px}
.faint-mark{position:absolute;left:0;right:0;top:132px;text-align:center;font-size:24px;font-weight:700;color:var(--faint);white-space:nowrap}
.letterhead-1 .footer-line{position:absolute;left:17px;right:12px;bottom:6px;display:flex;justify-content:space-between}

/* option 2 */
.letterhead-2{left:307px;top:40px;width:234px;height:302px}
.letterhead-2 .brand{position:absolute;left:0;right:0;top:14px;justify-content:center;font-size:11px}
.mission-foot{position:absolute;left:7px;top:246px;width:118px}
.letterhead-2 .contact{position:absolute;right:8px;bottom:6px;text-align:right;color:#fff}

/* option 3 */
.fax-sheet{left:567px;top:40px;width:234px;height:302px}
.fax-sheet .brand{position:absolute;left:19px;top:10px;font-size:11px}
.fax-sheet .head-contact{position:absolute;left:174px;top:10px}
.fax-title{position:absolute;left:17px;top:73px;font-size:16px;font-weight:400;color:#111}
.fax-fields{position:absolute;left:17px;top:100px;width:200px;display:grid;grid-template-columns:1fr 1fr;column-gap:18px;row-gap:5px}
.fax-field{font-size:4px;color:#444;border-bottom:.6px solid var(--rule);padding-bottom:1px;height:8px}
.fax-checks{position:absolute;left:17px;top:159px;display:flex;gap:10px}
.fax-check{font-size:4px;color:#444;display:flex;align-items:center;gap:3px}
.fax-check i{display:inline-block;width:5px;height:5px;border:.6px solid #555}
.fax-sheet .mission-side{position:absolute;right:6px;top:248px;width:112px;text-align:right}
.fax-sheet .mission-side h4{font-size:4.5px;color:var(--teal-dark);font-weight:700}

/* envelopes */
.envelope-back{left:876px;top:17px;width:260px;height:116px}
.envelope-back .brand{position:absolute;left:0;right:0;top:20px;justify-content:center;font-size:10px;color:#fff}
.envelope-back .brand .dot{background:#fff}
.envelope-open{left:818px;top:67px;width:289px;height:116px}
.envelope-open .brand{position:absolute;left:0;right:0;top:14px;justify-content:center;font-size:9px}
.envelope-front{left:846px;top:120px;width:261px;height:116px}
.envelope-front .brand{position:absolute;left:16px;top:6px;font-size:9px}
.envelope-front .address{position:absolute;left:10px;top:40px}
.envelope-front .web{position:absolute;right:10px;bottom:12px;font-size:4px;color:#fff;letter-spacing:.5px}

/* business cards */
.card-front{left:831px;top:265px;width:139px;height:79px}
.card-front .brand{position:absolute;left:10px;top:8px;font-size:8px}
.card-front .person{position:absolute;right:6px;top:6px;text-align:right}
.card-front .person b{display:block;font-size:4.5px;color:var(--orange)}
.card-front .person span{font-size:3.4px;color:var(--grey)}
.card-front .address{position:absolute;left:8px;top:38px}
.card-front .contact{position:absolute;right:5px;top:36px;text-align:right}
.card-back{left:984px;top:265px;width:138px;height:79px}
.card-back .brand{position:absolute;left:0;right:0;top:28px;justify-content:center;font-size:9px}
.card-back .web{position:absolute;left:0;right:0;top:46px;text-align:center;font-size:3.6px;color:var(--grey)}
</style>
</head>
<body>

<section class="sheet letterhead-1">
  <div class="brand"><span class="dot" style="width:6px;height:6px"></span>Moravel Swim</div>
  <div class="mission-top">
    <h4>mission statement</h4>
    <p class="tiny">"To provide aquatics programmes, for persons of all ages, that encourage physical fitness and wellness, build character and self-discipline, inspire camaraderie and promote civic mindedness and excellence."</p>
  </div>
  <div class="faint-mark" aria-hidden="true">Moravel Swim</div>
  <div class="footer-line tiny">
    <span>Lakeside Centre, 14 Harbour Rd, Eastvale</span>
    <span>+01 555 0142</span>
    <span>hello@moravelswim.org</span>
    <span>www.moravelswim.org</span>
  </div>
</section>

<section class="sheet letterhead-2">
  <div class="brand"><span class="dot" style="width:6px;height:6px"></span>Moravel Swim</div>
  <div class="mission-foot">
    <h4>mission statement</h4>
    <p class="tiny">"To provide aquatics programmes, for persons of all ages, that encourage physical fitness and wellness, build character and self-discipline, inspire camaraderie and promote civic mindedness and excellence."</p>
  </div>
  <svg class="swoosh" viewBox="0 0 234 50" height="50" preserveAspectRatio="none">
    <path d="M0 50 L0 49 C100 48 160 22 234 6 L234 50 Z" fill="var(--teal)"/>
    <path d="M0 46 C100 45 160 19 234 3" stroke="var(--orange)" stroke-width="2" fill="none"/>
    <path d="M0 43 C100 42 160 16 234 0.5" stroke="var(--orange)" stroke-width="1" fill="none"/>
  </svg>
  <div class="contact tiny" style="color:#fff">+01 555 0142<br>hello@moravelswim.org<br>www.moravelswim.org<br>Lakeside Centre, 14 Harbour Rd, Eastvale</div>
</section>

<section class="sheet fax-sheet">
  <div class="brand"><span class="dot" style="width:6px;height:6px"></span>Moravel Swim</div>
  <div class="head-contact tiny">+01 555 0142<br>hello@moravelswim.org<br>www.moravelswim.org<br>Lakeside Centre, 14 Harbour Rd,<br>Eastvale</div>
  <h1 class="fax-title">FAX</h1>
  <div class="fax-fields">
    <div class="fax-field">To :</div><div class="fax-field">From :</div>
    <div class="fax-field">Fax :</div><div class="fax-field">Pages :</div>
    <div class="fax-field">Phone :</div><div class="fax-field">Date :</div>
    <div class="fax-field">Re :</div><div class="fax-field">CC :</div>
  </div>
  <div class="fax-checks">
    <span class="fax-check"><i></i>Urgent</span>
    <span class="fax-check"><i></i>For Review</span>
    <span class="fax-check"><i></i>Please Comment</span>
    <span class="fax-check"><i></i>Please Reply</span>
    <span class="fax-check"><i></i>Please Recycle</span>
  </div>
  <div class="mission-side">
    <h4>mission statement</h4>
    <p class="tiny">"To provide aquatics programmes, for persons of all ages, that encourage physical fitness and wellness, build character and self-discipline, inspire camaraderie and promote civic mindedness and excellence."</p>
  </div>
  <svg class="swoosh" viewBox="0 0 234 22" height="22" preserveAspectRatio="none">
    <path d="M0 22 L0 15 C90 18 160 12 234 9 L234 22 Z" fill="var(--teal)"/>
    <path d="M0 12 C90 15 160 9 234 6" stroke="var(--orange)" stroke-width="1.8" fill="none"/>
    <path d="M0 8 C90 11 160 5 234 2" stroke="var(--orange)" stroke-width="1" fill="none"/>
  </svg>
</section>

<section class="envelope envelope-back">
  <svg width="260" height="116" viewBox="0 0 260 116" style="position:absolute;left:0;top:0">
    <path d="M0 0 H260 V38 L130 76 L0 38 Z" fill="var(--teal)"/>
  </svg>
  <div class="brand"><span class="dot" style="width:5px;height:5px"></span>Moravel Swim</div>
</section>

<section class="envelope envelope-open">
  <svg width="289" height="116" viewBox="0 0 289 116" style="position:absolute;left:0;top:0">
    <path d="M0 0 L144 44 L289 0" stroke="#666" stroke-width=".8" fill="none"/>
  </svg>
  <div class="brand"><span class="dot" style="width:5px;height:5px"></span>Moravel Swim</div>
</section>

<section class="envelope envelope-front">
  <div class="brand"><span class="dot" style="width:5px;height:5px"></span>Moravel Swim</div>
  <p class="address tiny">Lakeside Centre, 14 Harbour Rd,<br>Eastvale</p>
  <svg class="swoosh" viewBox="0 0 261 50" height="50" preserveAspectRatio="none">
    <path d="M0 50 L0 42 C100 44 180 22 261 18 L261 50 Z" fill="var(--teal)"/>
    <path d="M0 40 C100 42 180 20 261 15" stroke="var(--orange)" stroke-width="2.2" fill="none"/>
    <path d="M0 36 C100 38 180 16 261 11" stroke="var(--orange)" stroke-width="1" fill="none"/>
  </svg>
  <span class="web">www.moravelswim.org</span>
</section>

<section class="card card-front">
  <div class="brand"><span class="dot" style="width:4px;height:4px"></span>Moravel Swim</div>
  <div class="person"><b>Your Name</b><span>Title</span></div>
  <p class="address tiny">Lakeside Centre, 14 Harbour Rd,<br>Eastvale</p>
  <p class="contact tiny">+01 555 0142<br>+01 555 0143<br>hello@moravelswim.org<br>www.moravelswim.org</p>
  <svg class="swoosh" viewBox="0 0 139 16" height="16" preserveAspectRatio="none">
    <path d="M0 16 L0 13 C50 15 100 8 139 6 L139 16 Z" fill="var(--teal)"/>
    <path d="M0 11 C50 13 100 6 139 4" stroke="var(--orange)" stroke-width="1.2" fill="none"/>
    <path d="M0 8 C50 10 100 3 139 1" stroke="var(--orange)" stroke-width=".6" fill="none"/>
  </svg>
</section>

<section class="card card-back">
  <div class="brand"><span class="dot" style="width:5px;height:5px"></span>Moravel Swim</div>
  <p class="web">www.moravelswim.org</p>
</section>

<span class="option-label" style="left:167px">Option-1</span>
<span class="option-label" style="left:418px">Option-2</span>
<span class="option-label" style="left:677px">Option-3</span>

</body>
</html>
```